QM_radiance is a new upcoming amazing brand for modesty women , which started in 2016.

Design a page with all products and stating the title of the collection and style of the products and pricing.
Will need to create a column of upcoming events as well for customer to keep updated of our sales or flea

Target Market(s)

Hijabista, modesttrend

Number of Pages Required

5+ page

Requirements
Nice to have
• About Us
• Our brand represents classy and elegance yet it is comfortable and conservative to be worn everyday.
• Designs, and colours of fabrics chiffon , silk crepe and sateen silks and viscose cotton are exclusively chosen by QMradiance, imported from mainly high quality materials and sent for self manufactured.
• InsyaAllah#QMradiance

```html
<!DOCTYPE html>
<html lang="en">
<head>
<meta charset="utf-8">
<title>QM Radiance — Fashion Collections</title>
<link href="https://fonts.googleapis.com/css2?family=Oswald:wght@500;600&family=Open+Sans:wght@300;400;600;700&display=swap" rel="stylesheet">
<style>
:root{
  --green:#96c93d;
  --pink:#e7336f;
  --orange:#f7941d;
  --ink:#333;
  --muted:#8a8a8a;
  --line:#e3e3e3;
  --soft:#f0f0f0;
  --white:#fff;
}
*{margin:0;padding:0;box-sizing:border-box}
html,body{width:1200px;height:2597px;overflow:hidden;background:var(--white)}
body{position:relative;font-family:"Open Sans",Arial,sans-serif;color:var(--ink)}
.abs{position:absolute}

/* header */
.site-header{left:0;top:0;width:1200px;height:144px;background:var(--green)}
.top-links{right:99px;top:18px;display:flex;font-size:11px;color:var(--white);text-transform:uppercase}
.top-links span{padding:0 12px;border-left:1px solid rgba(255,255,255,.5)}
.top-links span:first-child{border-left:0}
.top-links span:last-child{padding-right:0}
.brand-name{left:99px;top:56px;font-family:"Oswald",sans-serif;font-weight:600;font-size:38px;line-height:50px;color:var(--white)}
.cart-box{left:637px;top:62px;width:177px;height:44px;border:1px solid rgba(255,255,255,.45);display:flex;align-items:center;padding:0 14px;gap:10px;color:var(--white);font-size:11px;font-weight:700}
.cart-box .caret{margin-left:auto}
.search-box{left:840px;top:62px;width:261px;height:44px;background:var(--white);display:flex;align-items:center;justify-content:space-between;padding:0 16px;font-size:12px;color:var(--muted)}

/* nav */
.main-nav{left:0;top:144px;width:1200px;height:57px;background:var(--pink)}
.main-nav ul{position:absolute;left:99px;top:0;display:flex;list-style:none;height:57px;border-left:1px solid rgba(255,255,255,.3)}
.main-nav li{display:flex;align-items:center;justify-content:center;color:var(--white);font-size:13px;text-transform:uppercase;border-right:1px solid rgba(255,255,255,.3)}

/* hero */
.hero-title{left:0;top:201px;width:367px;height:257px;background:var(--orange)}
.hero-sale{left:0;top:458px;width:367px;height:257px;background:var(--pink)}
.hero-title p,.hero-sale p{font-family:"Oswald",sans-serif;font-weight:600;color:var(--white);text-align:center;font-size:50px;line-height:62px}
.hero-title p{padding-top:36px}
.hero-sale p{padding-top:34px}
.hero-photo{left:367px;top:201px;width:833px;height:514px;background:linear-gradient(180deg,#f8f8fa 0%,#e6dadd 40%,#dcc9c1 65%,#e3e4e9 100%)}
.slider-dots{left:505px;top:676px;display:flex;gap:10px}
.slider-dots i{width:12px;height:12px;border-radius:50%;background:var(--white);border:1px solid #ccc}
.slider-dots i.on{background:var(--green);border-color:var(--green)}

/* section bars */
.bar{height:40px;color:var(--white);font-size:20px;font-weight:600;line-height:40px;padding-left:24px;text-transform:uppercase}
.bar.orange{background:var(--orange)}
.bar.green{background:var(--green)}

/* sidebar */
.brands{left:99px;top:774px;width:256px;height:367px;border:1px solid var(--line);border-top:0}
.brands .bar{margin:0 -1px}
.brands ul{list-style:none;padding:14px 0 0 24px}
.brands li{font-size:12.5px;color:#555;height:34px;line-height:34px;display:flex;align-items:center;gap:10px}
.special{left:99px;width:256px}
.special .photo{height:171px}
.special .info{background:var(--soft);text-align:center;padding-top:16px;height:80px}
.special .name{font-size:15px;color:#444}
.special .price{font-size:13px;margin-top:6px}
.special .price s{color:var(--orange);margin-right:40px}

/* product cards */
.card{width:227px;height:384px;border:1px solid var(--line)}
.card .photo{height:243px}
.card .title{font-size:13px;font-weight:600;line-height:21px;padding:20px 0 0 18px;text-transform:uppercase;color:#333}
.card .buy{display:flex;align-items:center;padding:18px 0 0 18px}
.card .price{font-size:19px;color:var(--orange);width:86px}
.card .details{display:flex;height:33px}
.card .details .icon{width:33px;background:var(--orange);display:flex;align-items:center;justify-content:center}
.card .details .label{width:69px;background:var(--green);color:var(--white);font-size:10px;font-weight:700;display:flex;align-items:center;justify-content:center}

/* promo banner */
.promo{left:0;top:1815px;width:1200px;height:436px;background:linear-gradient(90deg,#e9ebf1 0%,#e3e6ee 50%,#dadde6 100%)}
.promo-photo{left:320px;top:1838px;width:710px;height:413px;background:linear-gradient(90deg,#c9ccd2 0%,#2ea3c9 15%,#f3c4a8 35%,#e8a5b4 50%,#a31a33 65%,#d9bde9 85%,#e3cff0 100%);opacity:.9}
.promo-text{left:99px;top:1900px}
.promo-text .line1{font-size:39px;line-height:44px;color:var(--pink);font-weight:400}
.promo-text .line2{font-size:45px;line-height:56px;color:var(--green);font-weight:300;margin-top:14px}
.shop-now{left:99px;top:2093px;width:209px;height:51px;background:var(--orange);color:var(--white);font-size:22px;display:flex;align-items:center;justify-content:center}

/* footer */
.footer-col{top:2290px}
.footer-col h4{font-size:13.5px;font-weight:700;color:var(--green);text-transform:uppercase;margin-bottom:16px}
.footer-col p,.footer-col li{font-size:12px;line-height:24px;color:var(--muted);list-style:none}
.footer-col p+p{margin-top:10px}
.divider{top:2285px;width:1px;height:220px;background:var(--line)}
.newsletter{left:862px;top:2338px;width:239px;height:35px;border:1px solid var(--line);display:flex;align-items:center;justify-content:space-between;padding:0 14px;font-size:12px;color:var(--muted)}
.follow{left:862px;top:2394px;font-size:13.5px;font-weight:700;color:var(--green);text-transform:uppercase}
.social{top:2428px;width:38px;height:38px;border-radius:50%;background:var(--green)}
.bottom-bar{left:0;top:2528px;width:1200px;height:69px;background:var(--green)}
.copyright{left:99px;top:2551px;font-size:12.5px;color:var(--white)}
.pay{top:2552px;width:32px;height:20px;background:var(--white);border-radius:2px}
</style>
</head>
<body>

<header class="site-header abs">
  <div class="top-links abs"><span>Registration</span><span>Log in</span><span>Delivery</span><span>Checkout</span><span>My account</span></div>
  <div class="brand-name abs">QM RADIANCE</div>
  <div class="cart-box abs">
    <svg width="16" height="14" viewBox="0 0 16 14"><path d="M0 1h3l2 8h9l2-6H4.5" fill="none" stroke="#fff" stroke-width="1.8"/><circle cx="6" cy="12" r="1.4" fill="#fff"/><circle cx="13" cy="12" r="1.4" fill="#fff"/></svg>
    <span>CART&nbsp;&nbsp;(EMPTY)</span>
    <svg class="caret" width="8" height="6" viewBox="0 0 8 6"><path d="M1 1l3 3 3-3" fill="none" stroke="#fff" stroke-width="1.4"/></svg>
  </div>
  <div class="search-box abs">
    <span>Search entire store here...</span>
    <svg width="12" height="12" viewBox="0 0 12 12"><circle cx="5" cy="5" r="3.8" fill="none" stroke="#f7941d" stroke-width="1.8"/><path d="M8 8l3 3" stroke="#f7941d" stroke-width="1.8"/></svg>
  </div>
</header>

<nav class="main-nav abs">
  <ul>
    <li style="width:102px">Home</li>
    <li style="width:128px">Products</li>
    <li style="width:111px">Blog</li>
    <li style="width:138px">About us</li>
    <li style="width:172px">Collections</li>
    <li style="width:202px">Fashion clothings</li>
    <li style="width:149px">Contact us</li>
  </ul>
</nav>

<section class="hero-title abs"><p>2016<br>FASHION<br>COLLECTIONS</p></section>
<section class="hero-sale abs"><p>SALE<br>STARTING FROM<br>20 % OFF</p></section>
<div class="hero-photo abs" role="img" aria-label="Photograph of folded satin scarves in mauve, rose and beige on a pale background"></div>
<div class="slider-dots abs"><i class="on"></i><i></i><i></i></div>

<aside class="brands abs">
  <div class="bar orange">Brands</div>
  <ul>
    <li><svg width="8" height="8" viewBox="0 0 8 8"><path d="M1 1l3 3-3 3M4 1l3 3-3 3" fill="none" stroke="#555" stroke-width="1.1"/></svg>Nam libero tempore</li>
    <li><svg width="8" height="8" viewBox="0 0 8 8"><path d="M1 1l3 3-3 3M4 1l3 3-3 3" fill="none" stroke="#555" stroke-width="1.1"/></svg>Et harum quidem</li>
    <li><svg width="8" height="8" viewBox="0 0 8 8"><path d="M1 1l3 3-3 3M4 1l3 3-3 3" fill="none" stroke="#555" stroke-width="1.1"/></svg>Neque porro quisquam est</li>
    <li><svg width="8" height="8" viewBox="0 0 8 8"><path d="M1 1l3 3-3 3M4 1l3 3-3 3" fill="none" stroke="#555" stroke-width="1.1"/></svg>Quis autem vel eum</li>
    <li><svg width="8" height="8" viewBox="0 0 8 8"><path d="M1 1l3 3-3 3M4 1l3 3-3 3" fill="none" stroke="#555" stroke-width="1.1"/></svg>Nemo enim ipsam voluptatem</li>
    <li><svg width="8" height="8" viewBox="0 0 8 8"><path d="M1 1l3 3-3 3M4 1l3 3-3 3" fill="none" stroke="#555" stroke-width="1.1"/></svg>Lorem ipsum dolor sit</li>
    <li><svg width="8" height="8" viewBox="0 0 8 8"><path d="M1 1l3 3-3 3M4 1l3 3-3 3" fill="none" stroke="#555" stroke-width="1.1"/></svg>Duis aute irure dolor</li>
    <li><svg width="8" height="8" viewBox="0 0 8 8"><path d="M1 1l3 3-3 3M4 1l3 3-3 3" fill="none" stroke="#555" stroke-width="1.1"/></svg>Excepteur sint occaecat</li>
  </ul>
</aside>

<div class="bar orange abs" style="left:99px;top:1186px;width:256px">Specials</div>
<div class="special abs" style="top:1226px">
  <div class="photo" role="img" aria-label="Teal chiffon scarf with pearl flower trim" style="background:linear-gradient(135deg,#f4f4f6 20%,#2a9c86 45%,#24806f 60%,#eef0f2 85%)"></div>
  <div class="info"><div class="name">occaecati cupiditate</div><div class="price"><s>$150.00</s>$100.00</div></div>
</div>
<div class="special abs" style="top:1493px">
  <div class="photo" role="img" aria-label="Maroon polka dot scarf folded on white" style="height:159px;background:linear-gradient(135deg,#f4f4f6 20%,#6b3743 45%,#5a2a35 60%,#eef0f2 85%)"></div>
  <div class="info" style="height:88px;padding-top:18px"><div class="name">occaecati cupiditate</div><div class="price"><s>$200.00</s>$125.00</div></div>
</div>

<div class="bar green abs" style="left:381px;top:774px;width:720px">New products</div>

<article class="card abs" style="left:381px;top:850px">
  <div class="photo" role="img" aria-label="Model in a long blush pink gown" style="background:linear-gradient(90deg,#d9d9db 0%,#5a5a5e 35%,#d8b6ae 55%,#3d3d40 80%,#8b8b8e 100%)"></div>
  <div class="title">Molestias xcepturi sint<br>occaecati cupiditate</div>
  <div class="buy"><span class="price">$15.65</span><span class="details"><span class="icon"><svg width="14" height="12" viewBox="0 0 16 14"><path d="M0 1h3l2 8h9l2-6H4.5" fill="none" stroke="#fff" stroke-width="2"/><circle cx="6" cy="12" r="1.5" fill="#fff"/><circle cx="13" cy="12" r="1.5" fill="#fff"/></svg></span><span class="label">DETAILS</span></span></div>
</article>
<article class="card abs" style="left:627px;top:850px">
  <div class="photo" role="img" aria-label="Model in a silver sequin gown by a wooden door" style="background:linear-gradient(90deg,#3e352f 0%,#4b423b 30%,#c9c4c2 50%,#4b423b 70%,#3e352f 100%)"></div>
  <div class="title">Molestias xcepturi sint<br>occaecati cupiditate</div>
  <div class="buy"><span class="price">$15.65</span><span class="details"><span class="icon"><svg width="14" height="12" viewBox="0 0 16 14"><path d="M0 1h3l2 8h9l2-6H4.5" fill="none" stroke="#fff" stroke-width="2"/><circle cx="6" cy="12" r="1.5" fill="#fff"/><circle cx="13" cy="12" r="1.5" fill="#fff"/></svg></span><span class="label">DETAILS</span></span></div>
</article>
<article class="card abs" style="left:874px;top:850px">
  <div class="photo" role="img" aria-label="Model in a red sequin gown beside a car" style="background:linear-gradient(90deg,#cfcfd1 0%,#e9e9ea 30%,#c81c2c 50%,#e9e9ea 70%,#bdbdbf 100%)"></div>
  <div class="title">Molestias xcepturi sint<br>occaecati cupiditate</div>
  <div class="buy"><span class="price">$15.65</span><span class="details"><span class="icon"><svg width="14" height="12" viewBox="0 0 16 14"><path d="M0 1h3l2 8h9l2-6H4.5" fill="none" stroke="#fff" stroke-width="2"/><circle cx="6" cy="12" r="1.5" fill="#fff"/><circle cx="13" cy="12" r="1.5" fill="#fff"/></svg></span><span class="label">DETAILS</span></span></div>
</article>

<div class="bar green abs" style="left:381px;top:1280px;width:720px">Our collections</div>

<article class="card abs" style="left:381px;top:1356px">
  <div class="photo" role="img" aria-label="Model wearing a deep purple hijab" style="background:linear-gradient(180deg,#dde0e6 0%,#5a2448 40%,#4d1f3e 75%,#f1f1f3 100%)"></div>
  <div class="title">Molestias xcepturi sint<br>occaecati cupiditate</div>
  <div class="buy"><span class="price">$15.65</span><span class="details"><span class="icon"><svg width="14" height="12" viewBox="0 0 16 14"><path d="M0 1h3l2 8h9l2-6H4.5" fill="none" stroke="#fff" stroke-width="2"/><circle cx="6" cy="12" r="1.5" fill="#fff"/><circle cx="13" cy="12" r="1.5" fill="#fff"/></svg></span><span class="label">DETAILS</span></span></div>
</article>
<article class="card abs" style="left:627px;top:1356px">
  <div class="photo" role="img" aria-label="Model wearing a magenta hijab" style="background:linear-gradient(180deg,#dde0e6 0%,#b1216d 40%,#9c1c60 75%,#f1f1f3 100%)"></div>
  <div class="title">Molestias xcepturi sint<br>occaecati cupiditate</div>
  <div class="buy"><span class="price">$15.65</span><span class="details"><span class="icon"><svg width="14" height="12" viewBox="0 0 16 14"><path d="M0 1h3l2 8h9l2-6H4.5" fill="none" stroke="#fff" stroke-width="2"/><circle cx="6" cy="12" r="1.5" fill="#fff"/><circle cx="13" cy="12" r="1.5" fill="#fff"/></svg></span><span class="label">DETAILS</span></span></div>
</article>
<article class="card abs" style="left:874px;top:1356px">
  <div class="photo" role="img" aria-label="Model wearing a dusty rose hijab" style="background:linear-gradient(180deg,#dde0e6 0%,#c8677f 40%,#b85a72 75%,#f1f1f3 100%)"></div>
  <div class="title">Molestias xcepturi sint<br>occaecati cupiditate</div>
  <div class="buy"><span class="price">$15.65</span><span class="details"><span class="icon"><svg width="14" height="12" viewBox="0 0 16 14"><path d="M0 1h3l2 8h9l2-6H4.5" fill="none" stroke="#fff" stroke-width="2"/><circle cx="6" cy="12" r="1.5" fill="#fff"/><circle cx="13" cy="12" r="1.5" fill="#fff"/></svg></span><span class="label">DETAILS</span></span></div>
</article>

<section class="promo abs"></section>
<div class="promo-photo abs" role="img" aria-label="Row of pastel and jewel tone scarves hanging on a rail"></div>
<div class="promo-text abs">
  <div class="line1">FASHION<br>COLLECTION</div>
  <div class="line2">SALE OF 50 %</div>
</div>
<div class="shop-now abs">SHOP NOW</div>

<footer>
  <div class="footer-col abs" style="left:99px;width:220px">
    <h4>Information</h4>
    <p>Sed ut perspiciatis unde omnis iste natus error sit voluptatem accusan-tium doloremque laudantium.</p>
    <p>Ut enim ad minima veniam, quis nostrum exercitationem ullam...</p>
  </div>
  <div class="divider abs" style="left:355px"></div>
  <div class="footer-col abs" style="left:416px">
    <h4>Why buy from us</h4>
    <ul><li>Shipping &amp; Returns</li><li>Secure Shopping</li><li>International Shipping</li><li>Affiliates</li><li>Group Sales</li></ul>
  </div>
  <div class="divider abs" style="left:601px"></div>
  <div class="footer-col abs" style="left:663px">
    <h4>My account</h4>
    <ul><li>About Us</li><li>Customer Service</li><li>Template Settings</li><li>Privacy Policy</li><li>Site Map</li></ul>
  </div>
  <div class="divider abs" style="left:814px"></div>
  <div class="footer-col abs" style="left:862px"><h4>Newsletter sign up</h4></div>
  <div class="newsletter abs"><span>Enter Your Email</span><svg width="6" height="10" viewBox="0 0 6 10"><path d="M1 1l4 4-4 4" fill="none" stroke="#aaa" stroke-width="1.2"/></svg></div>
  <div class="follow abs">Follow us</div>
  <span class="social abs" style="left:862px"></span>
  <span class="social abs" style="left:913px"></span>
  <span class="social abs" style="left:965px"></span>
  <span class="social abs" style="left:1017px"></span>

  <div class="bottom-bar abs"></div>
  <div class="copyright abs">© 2016 QM Radiance. All Rights reserved.</div>
  <span class="pay abs" style="left:952px"></span>
  <span class="pay abs" style="left:986px"></span>
  <span class="pay abs" style="left:1020px"></span>
  <span class="pay abs" style="left:1054px"></span>
</footer>

</body>
</html>
```